Brand Identity Stationary Package

Hello I'm looking for a full branding package for my Property Management Company. I have a logo but looking to have the following
Business Card
Email signature
Facebook cover photo
Letterhead (word.doc)
#10 Envelope
Pocket Folder - link to 9x12 pocket folder design specs https://www.quillpress.ca/marketing-materials/presentation-folders
would like everything to match and be brand identifiable. The company looks after residential properties/apartments and some commercial properties. Attached is a zip of the files.
For Business Card
Name: Morgan Tillsey
Position: Operations Manager
Number: 1 (506) 384-2971
Email: Morgan@harbrook.ca
Website: Harbrook.ca
Industry/Entity Type
Property Management

```html
<!DOCTYPE html>
<html lang="en">
<head>
<meta charset="utf-8">
<title>Harbrook Business Card</title>
<link rel="stylesheet" href="https://fonts.googleapis.com/css2?family=Montserrat:wght@400;500;700&display=swap">
<style>
  :root {
    --page-bg: #d9d9d9;
    --card-white: #ffffff;
    --card-dark: #333333;
    --brand-green: #7ab52a;
    --ink: #111111;
    --ink-soft: #444444;
    --graphic-dark: #0a0a0a;
  }
  * { box-sizing: border-box; margin: 0; padding: 0; }
  html, body {
    width: 1200px; height: 800px; overflow: hidden;
    background: var(--page-bg);
    font-family: "Montserrat", Arial, sans-serif;
  }
  .stage {
    position: relative; width: 1200px; height: 800px;
    display: flex; align-items: center; justify-content: center; gap: 60px;
  }
  .card {
    position: relative; width: 525px; height: 300px;
    border-radius: 18px; overflow: hidden;
    box-shadow: 0 10px 28px rgba(0,0,0,0.18);
  }
  /* Front */
  .card--front { background: var(--card-white); }
  .edge-stripe {
    position: absolute; left: 0; top: 0; bottom: 0; width: 10px;
    background: var(--brand-green);
  }
  .edge-stripe__block {
    position: absolute; left: 0; top: 160px; width: 10px; height: 55px;
    background: var(--ink);
  }
  .house-graphic {
    position: absolute; right: 0; top: 0; width: 230px; height: 300px;
    background: linear-gradient(215deg, var(--graphic-dark) 0%, #2a2a2a 30%, rgba(255,255,255,0) 78%);
  }
  .contact {
    position: absolute; left: 40px; bottom: 32px;
  }
  .contact__name {
    color: var(--brand-green); font-weight: 700; font-size: 26px;
    letter-spacing: 0.5px; text-transform: uppercase; line-height: 1.1;
  }
  .contact__role {
    color: var(--ink-soft); font-size: 14px; font-weight: 400; margin-bottom: 14px;
  }
  .contact__line {
    display: flex; align-items: center; gap: 8px;
    color: var(--ink); font-size: 14px; font-weight: 500; line-height: 1.45;
  }
  .contact__line svg { width: 12px; height: 12px; flex: none; }
  .contact__web {
    margin-top: 12px; font-size: 17px; font-weight: 700; color: var(--ink);
  }
  .contact__web span { color: var(--brand-green); }
  /* Back */
  .card--back {
    background: var(--card-dark);
    display: flex; align-items: center; justify-content: center;
  }
  .brand-name {
    display: flex; align-items: center; gap: 14px;
  }
  .brand-name__mark {
    width: 22px; height: 22px; background: var(--brand-green);
  }
  .brand-name__text {
    color: #ffffff; font-size: 48px; font-weight: 700; letter-spacing: 4px;
    text-transform: uppercase;
  }
</style>
</head>
<body>
  <main class="stage">
    <section class="card card--front">
      <div class="edge-stripe"><div class="edge-stripe__block"></div></div>
      <div class="house-graphic" role="img" aria-label="Black house roof and window graphic fading into white"></div>
      <div class="contact">
        <h1 class="contact__name">Morgan Tillsey</h1>
        <p class="contact__role">Operations Manager</p>
        <p class="contact__line">
          <svg viewBox="0 0 24 24" aria-hidden="true"><path fill="#7ab52a" d="M6.6 10.8a15 15 0 0 0 6.6 6.6l2.2-2.2c.3-.3.7-.4 1-.2 1.1.4 2.3.6 3.6.6.6 0 1 .4 1 1V20c0 .6-.4 1-1 1A17 17 0 0 1 3 4c0-.6.4-1 1-1h3.5c.6 0 1 .4 1 1 0 1.3.2 2.5.6 3.6.1.3 0 .7-.2 1z"/></svg>
          1 (506) 384-2971
        </p>
        <p class="contact__line">
          <svg viewBox="0 0 24 24" aria-hidden="true"><path fill="#7ab52a" d="M2 5h20v14H2zm2 2v.5l8 5 8-5V7l-8 5z"/></svg>
          Morgan@harbrook.ca
        </p>
        <p class="contact__web">Har<span>brook.ca</span></p>
      </div>
    </section>

    <section class="card card--back">
      <div class="brand-name">
        <div class="brand-name__mark"></div>
        <span class="brand-name__text">Harbrook</span>
      </div>
    </section>
  </main>
</body>
</html>
```